Personal Injury Lawyer Billboard

I would like a design created featuring the image of the lawyer centered in the middle of the design.
To the left of the lawyer's image it should read "INJURED?"
To the right of the lawyer's image, it should read "CALL BRUNO!"
Under Call Bruno, include the phone number 318-555-0187.
At the bottom of the design include the lawyers information "Bruno Pemberly Accident & Injury Lawyers"
PLEASE REMOVED THE BACKGROUND IMAGERY OF THE PHOTO SUBMITTED. Also, the colors for this design should match the colors shown in the logo (navy, white and relective soft gold). Please use those color combinations in ways that best stand out.

```html
<!DOCTYPE html>
<html lang="en">
<head>
<meta charset="utf-8">
<title>Bruno Pemberly Accident &amp; Injury Lawyers – Billboard</title>
<link rel="stylesheet" href="https://fonts.googleapis.com/css2?family=Anton&display=swap">
<style>
  :root {
    --page-bg: #e9eaec;
    --gold: #cca36c;
    --navy: #1b2142;
    --suit-navy: #1f2a55;
    --skin: #b98a6c;
  }
  * { margin: 0; padding: 0; box-sizing: border-box; }
  html, body {
    width: 1200px;
    height: 999px;
    overflow: hidden;
    background: var(--page-bg);
  }
  .billboard {
    position: absolute;
    left: 30px;
    top: 262px;
    width: 1140px;
    height: 475px;
    background: var(--gold);
    overflow: hidden;
    font-family: "Anton", "Oswald", sans-serif;
    color: var(--navy);
  }
  .billboard p, .billboard h1 {
    white-space: nowrap;
    font-weight: 400;
  }
  .lawyer-photo {
    position: absolute;
    left: 320px;
    bottom: 0;
    width: 375px;
    height: 400px;
    border-radius: 150px 150px 0 0;
    background:
      radial-gradient(ellipse 70px 90px at 50% 28%, var(--skin) 0 98%, transparent 100%),
      linear-gradient(180deg, transparent 0 45%, var(--suit-navy) 45% 100%);
  }
  .headline {
    position: absolute;
    left: 700px;
    width: 400px;
    top: 40px;
    text-align: center;
    font-size: 112px;
    line-height: 1.1;
  }
  .call-to-action {
    position: absolute;
    left: 20px;
    width: 290px;
    top: 285px;
    text-align: center;
    line-height: 1.15;
  }
  .call-to-action .call-line { font-size: 38px; }
  .call-to-action .phone { font-size: 46px; letter-spacing: 0.5px; }
  .firm {
    position: absolute;
    left: 690px;
    width: 420px;
    top: 245px;
    text-align: center;
    line-height: 1.15;
  }
  .firm .firm-name { font-size: 42px; letter-spacing: 1.5px; }
  .firm .firm-tagline { font-size: 33px; }
</style>
</head>
<body>
  <main class="billboard">
    <div class="lawyer-photo" role="img" aria-label="Smiling lawyer in a navy suit and green tie raising a fist, background removed"></div>

    <h1 class="headline">Injured?</h1>

    <div class="call-to-action">
      <p class="call-line">Call Bruno!</p>
      <p class="phone">318-555-0187</p>
    </div>

    <div class="firm">
      <p class="firm-name">BRUNO PEMBERLY</p>
      <p class="firm-tagline">Accident &amp; Injury Lawyers</p>
    </div>
  </main>
</body>
</html>
```